SPA small billboard design and A frame sign

🎨 Creative Designers! We have an exciting opportunity for you! 🎨

Are you passionate about graphic design and have a knack for creating captivating pieces that convey a powerful message? Then this is your chance to shine!

We're seeking a spectacular design for the entrance sign of the prestigious Velora Spa, located within the lush Tamsenko Resort in Puerto Viejo, Costa Rica. This spa offers a unique experience where visitors can indulge in top-notch treatments and combine them with enjoying the resort's facilities, including a credit for the restaurant. It's the perfect oasis for relaxation and rejuvenation!

Project Details:

Entrance Sign: Size 100x64 cm. We want a captivating design that beckons people to enter and experience the luxury and serenity of the Velora Spa.
A-Frame Signs: Two A-frame signs, one to promote the spa's services and the other for spa days. Size 60x80 cm each.

More information about the Velora Spa: Download here: velora.tamsenko-example.com

We're looking for designs that reflect the essence of the Velora Spa and highlight its connection to nature, relaxation, and wellness!

🌟 Ready to be part of this exciting project? Submit your proposals today! 🌟

```html
<!DOCTYPE html>
<html lang="es">
<head>
<meta charset="utf-8">
<title>Velora Wellness Spa – Rótulo de entrada</title>
<link rel="stylesheet" href="https://fonts.googleapis.com/css2?family=Cormorant+Garamond:wght@500&family=Marcellus+SC&family=Montserrat:wght@600&display=swap">
<style>
  :root {
    --backdrop: #e2e2e2;
    --sign-white: #ffffff;
    --ink: #141414;
    --band-light: #ecdfcf;
    --band-mid: #b48a66;
    --band-dark: #6e3f22;
    --band-text: #fdf8f2;
    --photo-warm: #b07a4e;
    --photo-glow: #e6c59a;
    --photo-cool: #9cc8de;
    --blossom: #f7b9cd;
    --blossom-soft: #fde6ee;
  }
  * { margin: 0; padding: 0; box-sizing: border-box; }
  html, body {
    width: 1200px; height: 1200px; overflow: hidden;
    background: var(--backdrop);
  }
  .sign {
    position: absolute;
    left: 102px; top: 281px;
    width: 995px; height: 635px;
    background: var(--sign-white);
    overflow: hidden;
    box-shadow: 0 2px 6px rgba(0,0,0,0.18);
  }
  .service-band {
    position: absolute;
    left: 440px; top: 265px;
    width: 555px; height: 229px;
    background: linear-gradient(90deg, var(--band-light) 0%, var(--band-mid) 45%, var(--band-dark) 100%);
  }
  .service-list {
    position: absolute;
    right: 70px; top: 300px;
    list-style: none;
    text-align: right;
    font-family: "Marcellus SC", serif;
    font-size: 40px;
    line-height: 54px;
    color: var(--band-text);
    letter-spacing: 0.5px;
  }
  .photo-layer {
    position: absolute; left: 0; top: 0;
    width: 995px; height: 635px;
  }
  .brand {
    position: absolute;
    left: 670px; top: 62px;
    width: 262px;
    text-align: center;
    color: var(--ink);
  }
  .brand-name {
    font-family: "Cormorant Garamond", serif;
    font-weight: 500;
    font-size: 84px;
    line-height: 72px;
    letter-spacing: 1px;
  }
  .brand-tagline {
    font-family: "Montserrat", sans-serif;
    font-weight: 600;
    font-size: 14px;
    letter-spacing: 3px;
    margin-top: 6px;
  }
</style>
</head>
<body>
  <main class="sign">
    <div class="service-band"></div>

    <svg class="photo-layer" viewBox="0 0 995 635" xmlns="http://www.w3.org/2000/svg">
      <defs>
        <linearGradient id="massageScene" x1="0" y1="0" x2="0" y2="1">
          <stop offset="0" stop-color="var(--photo-warm)"/>
          <stop offset="0.35" stop-color="var(--photo-glow)"/>
          <stop offset="0.62" stop-color="var(--photo-warm)"/>
          <stop offset="1" stop-color="var(--photo-cool)"/>
        </linearGradient>
        <radialGradient id="blossomTone">
          <stop offset="0" stop-color="var(--blossom)"/>
          <stop offset="0.7" stop-color="var(--blossom)" stop-opacity="0.85"/>
          <stop offset="1" stop-color="var(--blossom-soft)" stop-opacity="0"/>
        </radialGradient>
      </defs>

      <path role="img" aria-label="Fotografía: terapeuta dando un masaje de espalda a una clienta en una cabina de spa de madera"
            d="M0 0 H372 Q448 0 448 60 L452 280 Q456 380 500 470 Q514 560 490 635 H0 Z"
            fill="url(#massageScene)"/>

      <circle role="img" aria-label="Ilustración de pétalo rosa" cx="300" cy="22" r="48" fill="url(#blossomTone)"/>
      <circle role="img" aria-label="Ilustración de flor de cerezo rosa" cx="472" cy="237" r="150" fill="url(#blossomTone)"/>
      <circle role="img" aria-label="Ilustración de pétalo rosa" cx="687" cy="585" r="70" fill="url(#blossomTone)"/>
      <circle role="img" aria-label="Ilustración de pétalo rosa" cx="975" cy="612" r="38" fill="url(#blossomTone)"/>
    </svg>

    <div class="brand">
      <div class="brand-name">velora</div>
      <div class="brand-tagline">WELLNESS SPA</div>
    </div>

    <ul class="service-list">
      <li>Masajes</li>
      <li>Los Especiales</li>
      <li>Pasa un Día de Spa</li>
    </ul>
  </main>
</body>
</html>
```